Marrowind Integrated Health Brochures (2)

We need two brochures about whiplash treatment to be designed. One is for referring physicians, the other is for the patients they refer. I'd like a few design elements to tie the two together, but also have them be easily distinguishable from one another.
In our region we are considered the top soft tissue injury clinic. We are trying to increase the awareness of our referring physicians to the fact that we have an exceptional rate of success treating acceleration/deceleration injuries from motor vehicle accidents.
We understand the emotional toll of whiplash. We understand how pain robs people of their vitality and motivation. We help victims of whiplash reclaim their health and vitality.
We use Quillpress.com for our printing.
Logo, trifold brochure template, and text(pdf files) have been up;oaded to this project.
The text we have provided is what we want. There are two versions of it. One is for the brochure for patients, and one is for the brochure for doctors.

Target Market(s)

Physicians that will refer Whiplash victims to our clinic for soft tissue injury treatment.

Industry/Entity Type

Health

Font styles to use
Serif

Requirements
Must have
• professional graphics that compliment the text.
• All AI files, graphic files etc.
• Colors that work with the Logo.
• Fonts for company name can be found on our website: www.marrowindintegratedhealth.com
Nice to have
• We'd like it to have a nice visual flow. We have only provided the text we want. Titles can be different if the design choices would make sense with better titles. We want it to be convincing and calming, and project our sensitivity to those suffering and also prject our confidence in our long history of curing the condition.

```html
<!DOCTYPE html>
<html lang="en">
<head>
<meta charset="utf-8">
<title>Marrowind Integrated Health – Whiplash Brochure Inside Panels</title>
<link href="https://fonts.googleapis.com/css2?family=Didact+Gothic&family=Questrial&display=swap" rel="stylesheet">
<style>
  :root {
    --ink: #2b2b2b;
    --heading: #1c1c1c;
    --sky: #86bbe0;
    --sky-pale: #b9d8ee;
    --ocean: #3d82c2;
    --paper: #ffffff;
  }
  html, body {
    margin: 0;
    padding: 0;
    overflow: hidden;
  }
  body {
    width: 1200px;
    height: 800px;
    background: var(--paper);
  }
  .brochure {
    position: relative;
    width: 1200px;
    height: 800px;
    overflow: hidden;
    background: var(--paper);
    color: var(--ink);
    font-family: "Didact Gothic", "Century Gothic", sans-serif;
  }
  .waves {
    position: absolute;
    inset: 0;
    width: 1200px;
    height: 800px;
  }
  .panel {
    position: absolute;
    text-align: center;
    white-space: nowrap;
  }
  .panel h2, .panel h3 {
    font-family: "Questrial", "Century Gothic", sans-serif;
    font-weight: 400;
    color: var(--heading);
    margin: 0;
  }
  .panel p {
    margin: 0;
  }

  /* left panel */
  .panel--toll {
    left: 24px;
    top: 42px;
    width: 396px;
  }
  .panel--toll h2 {
    font-size: 22px;
    line-height: 29px;
    margin-bottom: 21px;
  }
  .panel--toll p {
    font-size: 16.6px;
    line-height: 25px;
    letter-spacing: -0.2px;
  }
  .panel--toll p + p {
    margin-top: 25px;
  }

  /* middle panel */
  .panel--hope {
    left: 426px;
    top: 166px;
    width: 392px;
  }
  .panel--hope p {
    font-size: 16.8px;
    line-height: 25.2px;
    letter-spacing: -0.2px;
  }
  .panel--hope p + p {
    margin-top: 25px;
  }
  .panel--hope .dot {
    margin-top: 6px;
    line-height: 20px;
  }
  .panel--hope h3 {
    margin-top: 26px;
    font-size: 22px;
    line-height: 29px;
  }

  /* right panel */
  .panel--mission {
    left: 838px;
    top: 30px;
    width: 350px;
  }
  .panel--mission h2 {
    font-size: 22px;
    line-height: 29px;
  }
  .panel--mission .lead {
    margin-top: 16px;
    font-size: 15px;
    line-height: 20px;
  }
  .panel--mission .body {
    margin-top: 16px;
    font-size: 14.2px;
    line-height: 21.3px;
    letter-spacing: -0.15px;
  }
  .panel--mission strong {
    font-family: "Questrial", "Century Gothic", sans-serif;
    font-weight: 400;
    color: #111;
    font-size: 15.6px;
    letter-spacing: 0;
  }
</style>
</head>
<body>
<main class="brochure">
  <svg class="waves" viewBox="0 0 1200 800" aria-hidden="true">
    <path d="M0 0 H240 C160 22 80 42 0 66 Z" fill="var(--sky)"/>
    <path d="M0 56 C120 20 260 8 430 0" fill="none" stroke="var(--sky)" stroke-width="1.2"/>
    <path d="M80 30 C400 34 800 32 1200 40" fill="none" stroke="var(--sky)" stroke-width="1"/>
    <path d="M630 0 H1200 V42 C1040 20 860 6 630 0 Z" fill="var(--sky-pale)"/>
    <path d="M920 0 H1200 V34 C1110 16 1020 4 920 0 Z" fill="var(--sky)"/>
    <path d="M1080 0 H1200 V22 C1160 10 1120 3 1080 0 Z" fill="var(--ocean)"/>
    <path d="M0 704 C70 730 140 762 200 800 H0 Z" fill="var(--sky)"/>
    <path d="M0 770 C300 762 700 760 1200 772" fill="none" stroke="var(--sky)" stroke-width="1.2"/>
    <path d="M0 786 C200 778 500 772 760 770" fill="none" stroke="var(--sky-pale)" stroke-width="1"/>
    <path d="M760 800 C900 770 1060 745 1200 730 V800 Z" fill="var(--sky-pale)"/>
    <path d="M1000 800 C1080 770 1140 752 1200 740 V800 Z" fill="var(--sky)"/>
    <path d="M960 780 C1040 760 1120 745 1200 736" fill="none" stroke="var(--ocean)" stroke-width="1"/>
  </svg>

  <section class="panel panel--toll">
    <h2>The Emotional Toll of<br>“The Invisible Injury”</h2>
    <p>Suffering from a whiplash injury can have far<br>reaching affects. Many whiplash patients have<br>reported to us that the condition causes a<br>strain on the most important relationships in<br>their lives. When spouses, children, friends<br>and co-workers don't understand the whiplash<br>victim's pain or their change in temperament,<br>the social implications are clear. Since the injury<br>is invisible (no casts or crutches), those in<br>your life may not understand the significance<br>of your injury, which can lead to frustration and<br>stress in your relationships at home and at<br>work.</p>
    <p>Patients who have whiplash report that it is<br>often the little things they cannot do, like laundry,<br>house chores, computer work, and dressing<br>themselves, etc., that cause the most<br>stress. Feelings of fragility, fear, anger, vulnerability,<br>guilt, shame, weakness, and victimization<br>are common. It is also common for<br>them to feel misunderstood, isolated, and<br>alone in their suffering. This emotional stress<br>can actually slow the recovery process.</p>
  </section>

  <section class="panel panel--hope">
    <p>Most whiplash sufferers don’t want to be seen<br>as complainers, and so are often under<br>diagnosed with only neck pain<br>and headaches, which are usually<br>the most immediately<br>recognizable symptoms.<br>Whiplash victims need not despair.</p>
    <p>If you are suffering from a whiplash injury and<br>are having similar experiences, do not despair.<br>Our group of highly trained and experienced<br>professionals at Marrowind Integrated Health<br>have a proven record of successfully treating<br>this condition. We specialize in the treatment<br>of whiplash.</p>
    <p class="dot">.</p>
    <h3>We specialize in<br>the treatment of whiplash.</h3>
  </section>

  <section class="panel panel--mission">
    <h2>We can help you reclaim<br>you life.</h2>
    <p class="lead">Our Approach is in Our Mission</p>
    <p class="body">
      <strong>To Heal:</strong> We work to alleviate the symptoms<br>and the problems that cause<br>the symptoms. From the short term goal of defeating<br>the initial pain due to inflammation, to<br>the long term goal of correcting the structural<br>imbalance caused by muscle guarding, we<br>strive to return the patient to a pain free functional<br>state.<br>
      <strong>To Educate:</strong> Our patients gain a deeper<br>understanding<br>of how the human body works through<br>treatment, movement, stretching, and witnessing<br>the process of healing first hand. Many patients<br>consider the knowledge gained from<br>treatment at our clinic as an unanticipated silver<br>lining.<br>
      <strong>To Empower:</strong> Through the knowledge gained<br>during the process of treatment at our facility,<br>our patients are empowered, not only to avoid<br>pain and dysfunction, but, more importantly, to<br>move towards ever greater health.<br>
      We have earned and will work to keep the trust<br>of referring Doctors, Physical Therapists, and<br>other referring providers in the South<br>Fenwick/North Corran County area.<br>
      We have successfully treated thousands of<br>whiplash cases and look forward to putting our<br>expertise to work for you.
    </p>
  </section>
</main>
</body>
</html>
```